Wix Website design for my therapy business - Willowmere Group

I have started designing a Wix site and have a good idea of what I want.
I have set up the pages, created some design ideas, and inputted the copy. I need someone fabulous to finish off the design aspects. I like working closely with the designers, I was an interior designer in an old career.
I would like the site to be funky but professional. My Wix skills are limited, and I just can't achieve the look I am wanting without having to spend a lot of time learning. If it's easier to start over, that's ok providing you use the same colours, font, images etc. I have included a screenshot of the home page below. I have another site I need to start as soon as we have finished this one.
I am looking for someone who is a good listener and is has design flare. I am easy to get along with and will respond quickly.
I would like to set up SEO and have help in the future.
Let me know if you are the right person for the job.
Target Market(s)
Please needing help with their mental health and for therapy.
Industry/Entity Type
Mental health
Font styles to use
Other font styles liked:
- Futura light
Requirements
Must have
- be easy to navigate and be simple yet stylish
Nice to have
- I have set up the basics of the site - nice to haves are already on the site
Should not have
- old fashioned large chunks of text.

```html
<!DOCTYPE html>
<html lang="en">
<head>
<meta charset="utf-8">
<title>Willowmere Group – Therapy</title>
<link href="https://fonts.googleapis.com/css2?family=Poppins:wght@300;400;500;600;700&display=swap" rel="stylesheet">
<style>
:root{
  --brown:#9a8263;
  --brown-dark:#7d6a50;
  --orange:#f26a21;
  --ink:#1d1d1d;
  --text:#4a4a4a;
  --grey-band:#6d6d6d;
  --card:#f1f1f1;
  --footer:#1f1f1f;
  --white:#ffffff;
}
*{margin:0;padding:0;box-sizing:border-box}
html,body{width:1200px;height:4152px;overflow:hidden}
body{font-family:'Poppins',sans-serif;color:var(--text);background:var(--white);position:relative}
a{color:inherit;text-decoration:none}

/* top bar */
.topbar{position:absolute;left:0;top:0;width:1200px;height:112px;background:var(--white)}
.brand{position:absolute;left:40px;top:26px;display:flex;align-items:center;gap:10px}
.brand-mark{width:14px;height:14px;border-radius:50%;background:var(--brown)}
.brand-name{font-size:30px;font-weight:600;color:var(--ink);line-height:1}
.contact-top{position:absolute;right:40px;top:36px;display:flex;gap:30px;font-size:17px;color:var(--ink);font-weight:500}
.contact-top span{display:flex;align-items:center;gap:10px}
.ico{width:30px;height:30px;border-radius:50%;background:var(--ink);display:inline-flex;align-items:center;justify-content:center}

/* nav */
.nav{position:absolute;left:0;top:112px;width:1200px;height:48px;background:#000;display:flex;justify-content:center;align-items:center;gap:28px;font-size:16px;font-weight:500;color:var(--white)}

/* hero */
.hero{position:absolute;left:0;top:160px;width:1200px;height:640px;overflow:hidden}
.hero-photo{position:absolute;inset:0;background:radial-gradient(circle at 48% 30%,#fff2c9 0%,#f6c26b 20%,#d98a3a 48%,#8d5a2e 75%,#4d3320 100%)}
.hero-title{position:absolute;left:72px;top:160px;font-size:56px;font-weight:700;color:var(--ink);line-height:1.1}
.hero-text{position:absolute;left:72px;top:232px;width:620px;font-size:22px;color:var(--ink);line-height:1.35}
.btn{display:inline-block;background:var(--orange);color:var(--white);font-weight:600;border-radius:30px;font-size:17px;padding:12px 30px}
.btn-brown{background:var(--brown)}
.hero .btn-brown{position:absolute;left:72px;top:320px}
.hero-curve{position:absolute;left:0;bottom:0;width:1200px;height:170px}

/* appointment form */
.appt{position:absolute;left:800px;top:208px;width:332px;height:440px;background:rgba(255,255,255,.85);border-radius:14px;padding:16px 20px}
.appt h2{font-size:28px;font-weight:600;color:var(--ink);line-height:1.15}
.appt h2 em{font-style:normal;color:var(--brown)}
.field{height:44px;border:1px solid #bbb;border-radius:10px;background:var(--white);margin-top:14px;font-size:15px;padding:10px 16px;color:#444}
.field.msg{height:100px}
.appt .submit{display:block;margin-top:16px;height:44px;border-radius:22px;background:var(--orange);color:var(--white);font-weight:600;font-size:18px;text-align:center;line-height:44px}

/* welcome */
.welcome-img{position:absolute;left:84px;top:912px;width:480px;height:480px;border-radius:50%;border:12px solid var(--white);box-shadow:-18px 4px 0 0 var(--brown);background:linear-gradient(135deg,#d9d2c6,#8b7d6a 60%,#4f4539)}
.welcome-ring{position:absolute;left:76px;top:904px;width:496px;height:496px;border-radius:50%;border:10px solid #000;clip-path:polygon(50% 50%,100% 55%,100% 100%,0 100%,0 80%)}
.welcome-copy{position:absolute;left:608px;top:930px;width:560px}
.welcome-copy h2{font-size:44px;font-weight:600;color:var(--ink);line-height:1.15;white-space:nowrap}
.welcome-copy h2 span{color:var(--brown)}
.welcome-copy p{margin-top:20px;font-size:16px;line-height:1.55;width:520px}
.welcome-copy .btn{margin-top:30px}

/* services */
.services{position:absolute;left:0;top:1500px;width:1200px;height:860px}
.services svg.bg{position:absolute;inset:0}
.section-title{font-size:44px;font-weight:600;text-align:center;line-height:1}
.services .section-title{position:absolute;top:126px;width:100%;color:var(--white)}
.services .lead{position:absolute;top:194px;left:200px;width:800px;text-align:center;font-size:15px;line-height:1.55;color:#eee}
.svc-grid{position:absolute;top:286px;left:72px;display:flex;gap:24px}
.svc{width:246px;color:var(--white)}
.svc-img{height:184px;border-radius:6px}
.svc h3{font-size:20px;font-weight:600;margin-top:22px}
.svc p{font-size:14px;line-height:1.5;margin-top:8px;color:#ececec}

/* testimonials */
.testimonials .section-title{position:absolute;top:2396px;width:1200px;color:var(--ink)}
.testimonials .section-title span{color:var(--brown)}
.t-card{position:absolute;top:2500px;width:480px;height:300px;background:var(--card);border-radius:14px;text-align:center;padding:30px 36px}
.t-card p{font-size:16px;line-height:1.6;color:#555}
.t-card h4{margin-top:16px;font-size:16px;font-weight:600;color:var(--brown)}
.avatar{position:absolute;left:206px;top:252px;width:68px;height:68px;border-radius:50%;border:4px solid var(--white);background:linear-gradient(135deg,#c9b8a2,#6f5c47)}
.quote-mark{position:absolute;left:284px;top:262px;font-size:72px;font-weight:700;color:var(--brown-dark);line-height:1}
.arrow{position:absolute;font-size:40px;color:#666;line-height:1}

/* blog */
.blog{position:absolute;left:0;top:2960px;width:1200px;height:820px;background:var(--brown)}
.blog h2{position:absolute;left:72px;top:60px;font-size:44px;font-weight:600;color:var(--white)}
.blog-arrows{position:absolute;right:86px;top:64px;font-size:40px;color:var(--white);display:flex;gap:26px}
.post{position:absolute;top:150px;width:330px;color:var(--white)}
.post-img{height:236px;border-radius:16px}
.post time{display:block;margin-top:14px;font-size:14px;font-weight:500}
.post h3{font-size:20px;font-weight:600;line-height:1.3;margin-top:4px}
.post p{font-size:14px;line-height:1.5;margin-top:10px;color:#f3ece3}
.post .more{display:inline-block;margin-top:22px;background:var(--white);color:var(--ink);font-weight:600;font-size:15px;border-radius:24px;padding:8px 28px}
.post .center{text-align:center}

/* footer */
.footer{position:absolute;left:0;top:3740px;width:1200px;height:412px}
.footer svg{position:absolute;inset:0}
.newsletter{position:absolute;left:240px;top:48px;display:flex;align-items:center;gap:30px}
.newsletter h3{font-size:24px;font-weight:600;color:var(--white)}
.nl-box{display:flex;width:420px;height:50px;border:1px solid #999;border-radius:4px;overflow:hidden}
.nl-box span{flex:1;color:#bbb;font-size:15px;padding:14px 16px}
.nl-box b{width:50px;background:var(--orange);display:flex;align-items:center;justify-content:center}
.foot-brand{position:absolute;left:72px;top:148px;width:260px}
.foot-brand .brand{position:static}
.foot-brand .brand-name{color:var(--white);font-size:30px}
.foot-brand small{display:block;margin-top:22px;font-size:13px;color:#bbb;line-height:1.5}
.socials{display:flex;gap:14px;margin-top:18px}
.socials i{width:24px;height:24px;border-radius:4px;background:var(--brown)}
.fcol{position:absolute;top:150px}
.fcol h4{font-size:20px;font-weight:600;color:var(--brown)}
.fcol ul{list-style:none;margin-top:12px;font-size:15px;color:#ddd;line-height:2.1}
.fcol.two ul{columns:2;column-gap:50px;width:240px}
.addr li{display:flex;gap:12px;align-items:flex-start;line-height:1.6;margin-bottom:12px}
.addr i{flex:none;width:14px;height:14px;border-radius:50%;background:var(--brown);margin-top:5px}
</style>
</head>
<body>

<header class="topbar">
  <div class="brand"><i class="brand-mark"></i><span class="brand-name">Willowmere</span></div>
  <div class="contact-top">
    <span><i class="ico"><svg width="14" height="14" viewBox="0 0 24 24"><path fill="#fff" d="M6.6 10.8a15 15 0 0 0 6.6 6.6l2.2-2.2a1 1 0 0 1 1-.25 11.4 11.4 0 0 0 3.6.57 1 1 0 0 1 1 1V20a1 1 0 0 1-1 1A17 17 0 0 1 3 4a1 1 0 0 1 1-1h3.5a1 1 0 0 1 1 1c0 1.25.2 2.45.57 3.57a1 1 0 0 1-.25 1z"/></svg></i>+1 555-014-2287</span>
    <span><i class="ico"><svg width="15" height="12" viewBox="0 0 24 18"><path fill="#fff" d="M0 0h24v18H0zM2 2v1l10 7 10-7V2z"/></svg></i>hello@willowmeregroup.example</span>
  </div>
</header>

<nav class="nav">
  <a>Home</a><a>About Us</a><a>EMDR</a><a>Addictions</a><a>Betrayal Trauma</a><a>PTSD</a><a>Program List</a><a>Resources</a><a>Blog</a><a>Contact Us</a>
</nav>

<section class="hero">
  <div class="hero-photo" role="img" aria-label="Woman with raised arms in golden sunset light"></div>
  <h1 class="hero-title">The Willowmere Group</h1>
  <p class="hero-text">Nemo enim ipsam voluptatem quia voluptas aspernatur aut odit aut fugit, sed quia.</p>
  <a class="btn btn-brown">Read More</a>
  <svg class="hero-curve" viewBox="0 0 1200 170" preserveAspectRatio="none">
    <path d="M0 60 C260 200 520 150 760 100 C960 60 1100 80 1200 130 L1200 170 L0 170Z" fill="#fff"/>
    <path d="M0 60 C260 200 520 150 760 100 C960 60 1100 80 1200 130" fill="none" stroke="#9a8263" stroke-width="12"/>
  </svg>
</section>

<form class="appt">
  <h2>Book an<br><em>Appointment</em></h2>
  <div class="field">Name</div>
  <div class="field">Email Address</div>
  <div class="field">Phone No</div>
  <div class="field msg">Message</div>
  <span class="submit">Submit</span>
</form>

<section class="welcome">
  <div class="welcome-img" role="img" aria-label="Therapist talking with a client in a bright office"></div>
  <div class="welcome-ring"></div>
  <div class="welcome-copy">
    <h2>Welcome to<br><span>The Willowmere Group</span></h2>
    <p>Sed ut perspiciatis unde omnis iste natus error sit voluptatem accusantium doloremque laudantium, totam rem aperiam, eaque ipsa quae ab illo inventore veritatis et quasi architecto beatae vitae dicta sunt explicabo. Nemo enim ipsam voluptatem quia voluptas sit aspernatur aut odit aut fugit, sed quia consequuntur magni dolores eos qui ratione voluptatem sequi nesciunt.</p>
    <a class="btn">Read More</a>
  </div>
</section>

<section class="services">
  <svg class="bg" viewBox="0 0 1200 860" preserveAspectRatio="none">
    <path d="M0 40 C300 120 700 0 1200 60 L1200 790 C900 860 400 720 0 800Z" fill="#6d6d6d"/>
    <path d="M0 40 C300 120 700 0 1200 60" fill="none" stroke="#9a8263" stroke-width="10"/>
    <path d="M1200 790 C900 860 400 720 0 800" fill="none" stroke="#9a8263" stroke-width="10"/>
  </svg>
  <h2 class="section-title">Our Services</h2>
  <p class="lead">Sed ut perspiciatis unde omnis iste natus error sit voluptatem accusantium doloremque laudantium, totam rem aperiam, eaque ipsa quae ab illo inventore veritatis et quasi architecto beatae.</p>
  <div class="svc-grid">
    <article class="svc"><div class="svc-img" role="img" aria-label="Client in an EMDR therapy session" style="background:linear-gradient(135deg,#b9a892,#5e5245)"></div><h3>EMDR</h3><p>Neque porro quisquam est, qui dolorem ipsum quia dolor sit amet, consectetur enim ipsam voluptatem.</p></article>
    <article class="svc"><div class="svc-img" role="img" aria-label="Counsellor supporting a person with addiction" style="background:linear-gradient(135deg,#c9b89c,#7a6a55)"></div><h3>Addictions</h3><p>Neque porro quisquam est, qui dolorem ipsum quia dolor sit amet, consectetur enim ipsam voluptatem.</p></article>
    <article class="svc"><div class="svc-img" role="img" aria-label="Couple sitting apart after betrayal" style="background:linear-gradient(135deg,#c6c3bd,#6c6a66)"></div><h3>Betrayal Trauma</h3><p>Neque porro quisquam est, qui dolorem ipsum quia dolor sit amet, consectetur enim ipsam voluptatem.</p></article>
    <article class="svc"><div class="svc-img" role="img" aria-label="Therapist listening to a client with PTSD" style="background:linear-gradient(135deg,#d6d0c8,#8a8077)"></div><h3>PTSD</h3><p>Neque porro quisquam est, qui dolorem ipsum quia dolor sit amet, consectetur enim ipsam voluptatem.</p></article>
  </div>
</section>

<section class="testimonials">
  <h2 class="section-title">Our <span>Testimonials</span></h2>
  <span class="arrow" style="left:30px;top:2640px">&#8249;</span>
  <span class="arrow" style="right:30px;top:2640px">&#8250;</span>
  <article class="t-card" style="left:100px">
    <p>“ Sed ut perspiciatis unde omnis iste natus error sit voluptatem accusantium doloremque laudantium, totam rem aperiam, eaque ipsa quae ab illo inventore veritatis et quasi architecto beatae vitae dicta sunt explicabo..”</p>
    <h4>NAME HEADING</h4>
    <div class="avatar" role="img" aria-label="Client portrait"></div><span class="quote-mark">”</span>
  </article>
  <article class="t-card" style="left:620px">
    <p>“ Sed ut perspiciatis unde omnis iste natus error sit voluptatem accusantium doloremque laudantium, totam rem aperiam, eaque ipsa quae ab illo inventore veritatis et quasi architecto beatae vitae dicta sunt explicabo..”</p>
    <h4>NAME HEADING</h4>
    <div class="avatar" role="img" aria-label="Client portrait"></div><span class="quote-mark">”</span>
  </article>
</section>

<section class="blog">
  <h2>Blog Posts</h2>
  <div class="blog-arrows"><span>&#8249;</span><span>&#8250;</span></div>
  <article class="post" style="left:72px"><div class="post-img" role="img" aria-label="Couple in a counselling session" style="background:linear-gradient(135deg,#e2d6c4,#8c7458)"></div><time>Jul, 20, 2020</time><h3>Nemo enim ipsam voluptatem quia voluptas sit...</h3><p>Neque porro quisquam est, qui dolorem ipsum quia dolor sit amet, consectetur enim ipsam voluptatem.</p><div class="center"><a class="more">Read More</a></div></article>
  <article class="post" style="left:436px"><div class="post-img" role="img" aria-label="Support group joining hands" style="background:linear-gradient(135deg,#d9cab4,#5c4c3c)"></div><time>Jul, 20, 2020</time><h3>Nemo enim ipsam voluptatem quia voluptas sit...</h3><p>Neque porro quisquam est, qui dolorem ipsum quia dolor sit amet, consectetur enim ipsam voluptatem.</p><div class="center"><a class="more">Read More</a></div></article>
  <article class="post" style="left:800px"><div class="post-img" role="img" aria-label="Close-up of a hand raised in front of a face" style="background:linear-gradient(135deg,#e8c9b0,#8a6048)"></div><time>Jul, 20, 2020</time><h3>Nemo enim ipsam voluptatem quia voluptas sit...</h3><p>Neque porro quisquam est, qui dolorem ipsum quia dolor sit amet, consectetur enim ipsam voluptatem.</p><div class="center"><a class="more">Read More</a></div></article>
</section>

<footer class="footer">
  <svg viewBox="0 0 1200 412" preserveAspectRatio="none">
    <path d="M0 40 C400 0 800 10 1200 0 L1200 412 L0 412Z" fill="#1f1f1f"/>
    <path d="M0 40 C400 0 800 10 1200 0" fill="none" stroke="#9a8263" stroke-width="8"/>
  </svg>
  <div class="newsletter">
    <h3>Newsletter Sign Up</h3>
    <div class="nl-box"><span>Email Address</span><b><svg width="20" height="20" viewBox="0 0 24 24"><path fill="#fff" d="M2 21 23 12 2 3v7l15 2-15 2z"/></svg></b></div>
  </div>
  <div class="foot-brand">
    <div class="brand"><i class="brand-mark"></i><span class="brand-name">Willowmere</span></div>
    <small>Copyright 2023 © Willowmere Group<br>All Rights Reserved</small>
    <div class="socials"><i></i><i></i><i></i><i></i><i></i></div>
  </div>
  <div class="fcol two" style="left:374px"><h4>Site Map</h4><ul><li>Home</li><li>About Us</li><li>Services</li><li>Program List</li><li>Resources</li><li>Blog</li><li>Contact Us</li></ul></div>
  <div class="fcol" style="left:676px"><h4>Services</h4><ul><li>EMDR</li><li>Addictions</li><li>Betrayal Trauma</li><li>PTSD</li></ul></div>
  <div class="fcol" style="left:890px"><h4>Contact Address</h4><ul class="addr"><li><i></i>Excepteur sintoccaecat<br>Cupidatat non</li><li><i></i>+1 555-014-2287</li><li><i></i>hello@willowmeregroup.example</li></ul></div>
</footer>

</body>
</html>
```